Advertisement Coaching practice

I need an advertisement (to be printed in newspaper). I have a coaching practice where I offer coaching, workshops family constellations and relationship therapy. The ad needs to express calmness, inspiration to transform but also not dull and boring. It would be great if you could use the colors from my logo into the ad.

Dimensions are: 13,04 cm Width x 9,72 cm Height.

I will add my previous self-made ad, my company logo, a portrait photo of myself and the text I want to add. Also my contact details should be visible as well.

Requirements
Nice to have
• I have updated the brief with a flyer that I had previously made by a designer. It would be a nice to have if the ad ties in with that. You can also look at my website at www.fernbrook.nu to see what colors I used there.

```html
<!DOCTYPE html>
<html lang="nl">
<head>
<meta charset="utf-8">
<title>Coaching advertentie – Fernbrook</title>
<link rel="stylesheet" href="https://fonts.googleapis.com/css2?family=Poppins:wght@300;400;500;700;800&family=Barlow+Semi+Condensed:wght@700&display=swap">
<style>
  :root {
    --teal: #128890;
    --navy: #2a5b82;
    --gold: #f7d38a;
    --gold-pale: #fde6b4;
    --ink: #1c1c1c;
    --text: #333333;
    --white: #ffffff;
    --stage: #e9e6e6;
  }
  * { box-sizing: border-box; margin: 0; padding: 0; }
  html, body { width: 1200px; height: 1039px; overflow: hidden; }
  body {
    background: var(--stage);
    font-family: "Poppins", sans-serif;
    position: relative;
  }
  .ad {
    position: absolute;
    left: 0; top: 72px;
    width: 1200px; height: 895px;
    background: var(--white);
    overflow: hidden;
  }
  .ad > * { position: absolute; }
  .shapes { left: 0; top: 0; }

  .title-main {
    left: 52px; top: 60px;
    font-weight: 800; font-size: 114px; line-height: 1;
    color: var(--teal); letter-spacing: -1px;
  }
  .title-sub {
    left: 54px; top: 156px;
    font-family: "Barlow Semi Condensed", sans-serif;
    font-weight: 700; font-size: 58px; line-height: 1;
    color: var(--teal); letter-spacing: -0.5px;
  }
  .title-third {
    left: 54px; top: 206px;
    font-weight: 400; font-size: 48px; line-height: 1;
    color: var(--ink); letter-spacing: 12px;
  }
  .intro-bar { left: 55px; top: 272px; width: 6px; height: 77px; background: var(--teal); }
  .intro {
    left: 73px; top: 266px; width: 614px;
    font-size: 24.5px; line-height: 29px; color: var(--ink);
  }
  .support-heading {
    left: 55px; top: 386px;
    font-weight: 700; font-size: 32px; line-height: 1; color: var(--white);
    letter-spacing: -0.4px;
  }
  .support-heading .name { color: var(--gold); }

  .benefit {
    top: 434px; width: 230px;
    text-align: center; color: var(--white);
    font-size: 19.5px; line-height: 23.4px;
  }
  .benefit-icon {
    display: block; margin: 0 auto 9px;
    width: 72px; height: 72px;
  }
  .benefit--patterns { left: 15px; }
  .benefit--conflict { left: 246px; }
  .benefit--connection { left: 494px; }
  .divider { top: 440px; height: 144px; border-left: 1.5px dashed rgba(255,255,255,0.55); }
  .divider--one { left: 241px; }
  .divider--two { left: 486px; }

  .details {
    left: 218px; top: 649px;
    font-size: 15px; line-height: 19.5px; color: var(--text); letter-spacing: -0.2px;
    white-space: nowrap;
  }
  .cta {
    left: 218px; top: 724px;
    font-family: "Barlow Semi Condensed", sans-serif;
    font-weight: 700; font-size: 27.5px; line-height: 24px; text-transform: uppercase;
    white-space: nowrap;
  }
  .cta-line1 { color: var(--teal); display: block; }
  .cta-line2 { color: var(--navy); display: block; }

  .name-tab {
    left: 195px; top: 792px; width: 250px; height: 48px;
    background: var(--navy);
    border-radius: 22px 0 0 0;
    clip-path: polygon(0 0, 94% 0, 100% 100%, 0 100%);
    color: var(--white); font-weight: 700; font-size: 20px;
    padding: 10px 0 0 22px;
  }
  .base-line { left: 132px; top: 839px; width: 1017px; height: 3px; background: var(--navy); }

  .contact {
    left: 453px; top: 812px;
    display: flex; gap: 12px; align-items: center;
    font-size: 16px; color: var(--ink); white-space: nowrap;
  }
  .contact-item { display: flex; align-items: center; gap: 6px; }
  .contact-item svg { width: 14px; height: 14px; }

  .brand { left: 975px; top: 707px; width: 172px; text-align: center; }
  .brand-mark {
    display: block; margin: 0 auto 8px;
    width: 52px; height: 52px; border-radius: 50%;
    border: 2px solid var(--teal);
  }
  .brand-name { font-weight: 300; font-size: 31px; line-height: 1; color: #555555; }
</style>
</head>
<body>
<div class="ad">
  <svg class="shapes" width="1200" height="895" viewBox="0 0 1200 895">
    <defs>
      <linearGradient id="bandGrad" x1="0" y1="0" x2="1" y2="0">
        <stop offset="0" stop-color="#1a858b"/>
        <stop offset="1" stop-color="#1e959a"/>
      </linearGradient>
      <linearGradient id="roomGrad" x1="0" y1="0" x2="1" y2="1">
        <stop offset="0" stop-color="#e6e5e0"/>
        <stop offset="0.55" stop-color="#b8a89a"/>
        <stop offset="1" stop-color="#5a4e46"/>
      </linearGradient>
      <linearGradient id="portraitGrad" x1="0" y1="0" x2="0" y2="1">
        <stop offset="0" stop-color="#7a6a58"/>
        <stop offset="0.6" stop-color="#a87e62"/>
        <stop offset="1" stop-color="#c7cbd8"/>
      </linearGradient>
    </defs>
    <rect x="0" y="375" width="900" height="260" fill="url(#bandGrad)"/>
    <circle cx="1059" cy="312" r="366" fill="var(--gold-pale)"/>
    <circle cx="1036" cy="339" r="337" fill="#ffffff"/>
    <g role="img" aria-label="Foto: workshop in een lichte zaal, een coach staat voor een groep deelnemers">
      <circle cx="1036" cy="339" r="327" fill="url(#roomGrad)"/>
    </g>
    <circle cx="109" cy="740" r="100" fill="var(--navy)"/>
    <g role="img" aria-label="Portretfoto van Mirela Doornbos">
      <circle cx="113" cy="736" r="90" fill="url(#portraitGrad)"/>
    </g>
  </svg>

  <h1 class="title-main">COACHING</h1>
  <div class="title-sub">FAMILIEOPSTELLINGEN &amp;</div>
  <div class="title-third">RELATIETHERAPIE</div>

  <div class="intro-bar"></div>
  <p class="intro">Trauma’s en negatieve ervaringen vormen ons en blijven nog lang voelbaar. Ze kunnen groei of geluk in de weg staan.</p>

  <h2 class="support-heading">Ik ben <span class="name">Mirela</span> en ondersteun je bij het:</h2>

  <div class="benefit benefit--patterns">
    <svg class="benefit-icon" viewBox="0 0 74 74">
      <circle cx="37" cy="37" r="35" fill="#fff"/>
      <circle cx="37" cy="37" r="30" fill="none" stroke="var(--teal)" stroke-width="2"/>
      <path d="M29 56v-8c-5-3-7-8-7-13 0-9 7-15 15-15s14 6 14 13l4 7h-4v6h-7v10" fill="none" stroke="var(--teal)" stroke-width="2" stroke-linejoin="round"/>
      <circle cx="38" cy="33" r="5" fill="none" stroke="var(--teal)" stroke-width="2"/>
    </svg>
    Doorbreken van<br>belemmerende<br>patronen
  </div>
  <div class="divider divider--one"></div>
  <div class="benefit benefit--conflict">
    <svg class="benefit-icon" viewBox="0 0 74 74">
      <circle cx="37" cy="37" r="35" fill="#fff"/>
      <circle cx="37" cy="37" r="30" fill="none" stroke="var(--teal)" stroke-width="2"/>
      <rect x="22" y="38" width="14" height="12" rx="4" fill="none" stroke="var(--teal)" stroke-width="2"/>
      <rect x="38" y="24" width="14" height="12" rx="4" fill="none" stroke="var(--teal)" stroke-width="2"/>
      <path d="M33 30l-3-3M30 34h-4M46 44l3 3M44 48v4" stroke="var(--teal)" stroke-width="2" stroke-linecap="round"/>
    </svg>
    Beter omgaan<br>met conflicten
  </div>
  <div class="divider divider--two"></div>
  <div class="benefit benefit--connection">
    <svg class="benefit-icon" viewBox="0 0 74 74">
      <circle cx="37" cy="37" r="35" fill="#fff"/>
      <circle cx="37" cy="37" r="30" fill="none" stroke="var(--teal)" stroke-width="2"/>
      <circle cx="37" cy="22" r="4" fill="none" stroke="var(--teal)" stroke-width="2"/>
      <circle cx="25" cy="44" r="4" fill="none" stroke="var(--teal)" stroke-width="2"/>
      <circle cx="49" cy="44" r="4" fill="none" stroke="var(--teal)" stroke-width="2"/>
      <path d="M37 28v8M37 36l-10 4M37 36l10 4M19 54c0-4 3-6 6-6s6 2 6 6M43 54c0-4 3-6 6-6s6 2 6 6" fill="none" stroke="var(--teal)" stroke-width="2"/>
    </svg>
    In gezonde<br>verbinding met elkaar<br>als koppel of met<br>anderen komen
  </div>

  <p class="details">Maandelijks geef ik workshops familieopstellingen. Ook houd ik themasessies<br>rond adoptie, moeder-dochterdynamiek of relaties. Ook bied ik individuele coaching,<br>relatietherapie en retraites aan.</p>

  <p class="cta">
    <span class="cta-line1">Kijk op de website voor meer info of</span>
    <span class="cta-line2">neem contact op en ontdek wat het beste bij jou past</span>
  </p>

  <div class="name-tab">Mirela Doornbos</div>
  <div class="base-line"></div>

  <div class="contact">
    <span class="contact-item">
      <svg viewBox="0 0 14 14"><path d="M3 1l2 3-1.5 1.5c.8 2 2 3.2 4 4L9 8l3 2-1.5 2.5C5.5 12 2 8.5 1.5 3z" fill="var(--teal)"/></svg>
      06-41 27 58 93
    </span>
    <span class="contact-item">
      <svg viewBox="0 0 14 14"><rect x="1" y="3" width="12" height="9" fill="none" stroke="var(--teal)" stroke-width="1.5"/><path d="M1 3l6 5 6-5" fill="none" stroke="var(--teal)" stroke-width="1.5"/></svg>
      info@fernbrook.nu
    </span>
    <span class="contact-item">
      <svg viewBox="0 0 14 14"><circle cx="7" cy="7" r="5.5" fill="none" stroke="var(--teal)" stroke-width="1.5"/><path d="M1.5 7h11M7 1.5c-3 3-3 8 0 11M7 1.5c3 3 3 8 0 11" fill="none" stroke="var(--teal)" stroke-width="1.2"/></svg>
      www.fernbrook.nu
    </span>
  </div>

  <div class="brand">
    <span class="brand-mark"></span>
    <div class="brand-name">fernbrook</div>
  </div>
</div>
</body>
</html>
```